Fiber Optic Internet flyer promotion Winter 2016-2017

I am looking for a marketing flyer that will not be folded, single sided that will advertise a Fiber Optic internet promotion that we are currently running.

The design should be clean, flow well, quickly grab attention, and if a very few short seconds list what the promotion is, and direct them to contact us.

It needs to list a few features of the promotion, but does not need to be in this order and should flow well with the flyer
1.) Fiber Optic Internet
2.) 100 Mbits for $140 /month or 150 Mbits for $190 /month
3.) Free construction cost up to $10,000, limited funds available.
4.) Limited time offer. Must commit before funds run out.

(555) 274-3916, www.kelvoranet.example

Target Market(s)

Small to large business

Industry/Entity Type

Internet Service Provider

Requirements
Must have
• Eye catching appeal. Quickly convey the message of the promotion and our company name and phone number.
Should not have
• Our company is primarily a wireless ISP. This promotion is all about Fiber Optic. I do not want to draw attention to the "wireless" portion of our business with this flyer.

```html
<!DOCTYPE html>
<html lang="en">
<head>
<meta charset="utf-8">
<title>Kelvora Networks – Fiber Optic Internet Promotion</title>
<link rel="stylesheet" href="https://fonts.googleapis.com/css2?family=Open+Sans:wght@300;400;600;700&display=swap">
<style>
  :root {
    --night: #000000;
    --fiber-blue: #1aa6e8;
    --fiber-deep: #0a3f73;
    --paper: #ffffff;
    --ink: #1b1b1b;
    --navy: #2b3575;
    --signal-red: #d42a34;
  }
  * { margin: 0; padding: 0; box-sizing: border-box; }
  html, body { width: 1200px; height: 848px; overflow: hidden; background: var(--paper); }
  body { font-family: "Open Sans", Arial, sans-serif; }

  .flyer { position: relative; width: 1200px; height: 848px; overflow: hidden; }

  .hero {
    position: absolute; left: 0; top: 0; width: 1200px; height: 509px;
    background: var(--night);
  }
  .hero__fiber-art {
    position: absolute; left: 0; top: 0; width: 560px; height: 509px;
    background:
      radial-gradient(ellipse 70% 60% at 0% 45%, rgba(26,166,232,0.85) 0%, rgba(10,63,115,0.55) 45%, rgba(0,0,0,0) 100%),
      linear-gradient(100deg, rgba(26,166,232,0.35) 0%, rgba(0,0,0,0) 70%);
  }
  .hero__headline {
    position: absolute; left: 342px;
    color: var(--paper); font-weight: 600; font-size: 44px; letter-spacing: 0.5px;
    line-height: 1; white-space: nowrap;
    text-shadow: 3px 3px 3px rgba(120,120,120,0.8);
  }
  .hero__headline--offer { top: 192px; }
  .hero__headline--commit { top: 300px; }

  .features {
    position: absolute; left: 0; top: 509px; width: 1200px; height: 239px;
    background: var(--paper);
  }
  .features__list { list-style: none; position: absolute; left: 48px; top: 36px; }
  .features__item {
    display: flex; align-items: center; height: 26px; margin-bottom: 28px;
    font-size: 22px; font-weight: 600; color: var(--ink); white-space: nowrap;
  }
  .features__item:nth-child(2) { margin-bottom: 24px; }
  .dot {
    display: inline-block; width: 22px; height: 22px; border-radius: 50%;
    background: var(--signal-red); margin-right: 12px; flex: none;
  }

  .brand {
    position: absolute; left: 834px; top: 640px; width: 330px;
    display: flex; align-items: center; gap: 12px;
    color: var(--navy); font-weight: 700; font-size: 31px; white-space: nowrap;
  }
  .brand__mark { width: 22px; height: 22px; border-radius: 50%; background: var(--navy); flex: none; }

  .contact-bar {
    position: absolute; left: 0; top: 748px; width: 1200px; height: 100px;
    background: var(--navy); color: var(--paper);
  }
  .contact {
    position: absolute; top: 29px; display: flex; align-items: center;
    font-size: 36px; line-height: 42px; white-space: nowrap;
  }
  .contact .dot { width: 24px; height: 24px; margin-right: 16px; }
  .contact__label { font-weight: 300; margin-right: 10px; }
  .contact__value { font-weight: 600; }
  .contact--phone { left: 50px; }
  .contact--web { left: 626px; }
</style>
</head>
<body>
<main class="flyer">
  <section class="hero">
    <div class="hero__fiber-art" role="img" aria-label="Glowing blue fiber optic strands streaming in from the left with coloured light points"></div>
    <h1 class="hero__headline hero__headline--offer">LIMITED TIME OFFER</h1>
    <h2 class="hero__headline hero__headline--commit">COMMIT BEFORE FUNDS RUN OUT</h2>
  </section>

  <section class="features">
    <ul class="features__list">
      <li class="features__item"><span class="dot"></span>Fiber Optic Internet</li>
      <li class="features__item"><span class="dot"></span>100 Mbits for $140 /month or 150 Mbits for $190 /month</li>
      <li class="features__item"><span class="dot"></span>Free construction cost up to $10,000, limited funds available</li>
    </ul>
  </section>

  <div class="brand"><span class="brand__mark"></span>Kelvora Networks</div>

  <footer class="contact-bar">
    <div class="contact contact--phone"><span class="dot"></span><span class="contact__label">CALL</span><span class="contact__value">(555) 274-3916</span></div>
    <div class="contact contact--web"><span class="dot"></span><span class="contact__label">VISIT</span><span class="contact__value">www.kelvoranet.example</span></div>
  </footer>
</main>
</body>
</html>
```